Velmora Commercial Finance Information Brochure

This brochure will be sent out to clients via A4 PDF on an email to showcase what our company has to offer. We are a commercial finance brokerage, that specialises in property finance. We would like to see designs following our colour scheme. The final design should demonstrate our professionalism and reliability.
I have attached our logo and also a few bullet points on our information and what we can offer. These can be slightly reworded for conciseness. Or leave the text sections as filler and I can fill these in.
I have also attached an overview of our colour scheme and design styling for your consideration.
Target Market(s)
Property Developers
Industry/Entity Type
Financial Services
Look and feel
Each slider illustrates characteristics of the customer's brand and the style your logo design should communicate.

```html
<!DOCTYPE html>
<html lang="en">
<head>
<meta charset="utf-8">
<title>Velmora Finance – Information Brochure</title>
<link href="https://fonts.googleapis.com/css2?family=Montserrat:wght@500;700;800&family=Roboto+Condensed:wght@400;500;700&display=swap" rel="stylesheet">
<style>
  :root {
    --brand-blue: #1f3d9c;
    --brand-green: #23863f;
    --ink: #1b1b1b;
    --paper: #ffffff;
    --backdrop: #e9ecf3;
  }
  * { box-sizing: border-box; margin: 0; padding: 0; }
  html, body { width: 1200px; height: 898px; overflow: hidden; background: var(--backdrop); }
  .stage { position: relative; width: 1200px; height: 898px; }
  .brochure {
    position: absolute; left: 293px; top: 14px;
    width: 1036px; height: 1468px;
    transform: scale(0.5926); transform-origin: top left;
    background: var(--paper); overflow: hidden;
    font-family: "Roboto Condensed", Arial, sans-serif;
  }
  .hero { position: absolute; left: 0; top: 0; width: 1036px; height: 580px; }
  .hero-photo {
    position: absolute; left: 0; top: 0; width: 100%; height: 100%;
    background:
      linear-gradient(90deg, rgba(40,80,150,.55) 0%, rgba(160,200,230,.2) 35%, rgba(255,255,255,.3) 55%, rgba(60,160,180,.6) 75%, rgba(140,200,220,.3) 100%),
      linear-gradient(180deg, #a9dcef 0%, #d9eef7 50%, #7fbfd6 100%);
  }
  .hero-shape { position: absolute; left: 0; top: 0; }
  .brand-name {
    position: absolute; left: 60px; top: 58px;
    font-family: "Montserrat", Arial, sans-serif; font-weight: 700;
    font-size: 44px; letter-spacing: 1px; color: var(--paper);
    line-height: 1;
  }
  .intro { position: absolute; left: 0; top: 600px; width: 1036px; text-align: center; }
  .headline {
    font-family: "Montserrat", Arial, sans-serif; font-weight: 800;
    font-size: 50px; line-height: 61px; color: var(--brand-blue);
    text-transform: uppercase;
  }
  .tagline {
    margin-top: 12px;
    font-family: "Montserrat", Arial, sans-serif; font-weight: 500;
    font-size: 33px; color: var(--brand-blue);
  }
  .body-col {
    position: absolute; top: 788px; width: 449px;
    font-size: 19px; line-height: 24.4px; color: var(--ink);
    text-align: justify;
  }
  .body-col p + p { margin-top: 16px; }
  .body-col.left { left: 52px; }
  .body-col.right { left: 534px; }
  .products-band { position: absolute; left: 0; top: 1088px; width: 1036px; height: 175px; background: var(--brand-green); }
  .products-rule { position: absolute; left: 0; top: 1333px; width: 1036px; height: 7px; background: var(--brand-green); }
  .products-label {
    position: absolute; left: 421px; top: 1073px; width: 192px; height: 38px;
    background: var(--brand-blue); border-radius: 8px;
    font-family: "Montserrat", Arial, sans-serif; font-weight: 700;
    font-size: 20px; line-height: 38px; color: var(--paper); text-align: center;
  }
  .product { position: absolute; top: 1128px; width: 288px; }
  .product-title {
    font-family: "Montserrat", Arial, sans-serif; font-weight: 700;
    font-size: 17px; color: var(--paper); text-align: center; height: 37px; line-height: 26px;
    white-space: nowrap;
  }
  .product-photo { height: 149px; border: 5px solid var(--paper); }
  .p1 { left: 54px; } .p2 { left: 367px; width: 286px; } .p3 { left: 697px; }
  .p1 .product-photo { background: linear-gradient(135deg, #3a2e26 0%, #cfc9bd 45%, #f2eee6 65%, #5a4a3d 100%); }
  .p2 .product-photo { background: linear-gradient(180deg, #4aa7d8 0%, #a9d8ee 45%, #c9913c 70%, #2f6fa8 100%); }
  .p3 .product-photo { background: linear-gradient(135deg, #f3d27e 0%, #d89a45 55%, #b56a28 100%); }
  .footer { position: absolute; left: 0; top: 1343px; width: 1036px; height: 125px; background: var(--brand-blue); color: var(--paper); }
  .contact-line {
    position: absolute; left: 26px; display: flex; align-items: center; gap: 8px;
    font-size: 19px; font-weight: 700; white-space: nowrap;
  }
  .contact-line.address { top: 32px; }
  .contact-line.reach { top: 63px; gap: 6px; }
  .contact-line.reach .item { display: inline-flex; align-items: center; gap: 6px; margin-right: 8px; }
  .call-badge { position: absolute; left: 716px; top: 29px; }
  .call-note { position: absolute; left: 786px; top: 26px; font-size: 21px; font-weight: 500; }
  .call-number { position: absolute; left: 784px; top: 48px; font-size: 38px; font-weight: 700; letter-spacing: .5px; }
</style>
</head>
<body>
<div class="stage">
  <article class="brochure">
    <header class="hero">
      <div class="hero-photo" role="img" aria-label="Photo of a business handshake over a desk beside a high-rise under construction with tower cranes"></div>
      <svg class="hero-shape" width="1036" height="240" viewBox="0 0 1036 240">
        <path d="M0 0 H1036 V148 Q560 122 0 190 Z" fill="#1f3d9c"/>
        <path d="M0 190 Q560 122 1036 148 V156 Q560 138 0 198 Z" fill="#ffffff"/>
        <path d="M0 198 Q560 138 1036 156 V160 Q560 152 0 216 Z" fill="#23863f"/>
      </svg>
      <div class="brand-name">VELMORA FINANCE</div>
    </header>

    <section class="intro">
      <h1 class="headline">A Whole New World of<br>Financial Solutions</h1>
      <p class="tagline">What sets us apart? Well, we’ve walked in your shoes.</p>
    </section>

    <div class="body-col left">
      <p>As former lenders and developers ourselves, we intimately understand the inefficiencies that plague many brokers in the market today. We’ve experienced the frustration of tight time limits on deals and the exasperating feeling of brokers wasting precious time collecting information. It’s enough to drive developers and lenders insane!</p>
      <p>That’s why we founded Velmora Finance - to be the efficient and reliable link that connects developers and lenders.</p>
    </div>
    <div class="body-col right">
      <p>We’ve streamlined our processes to eliminate unnecessary hurdles, enabling clear and swift communication between all parties involved. No more wasted time. No more unnecessary stress.</p>
      <p>With our expertise and industry insights, we’ve developed a unique approach that simplifies the financing journey. From the initial consultation to the final funding, we’re here to guide you every step of the way. Our goal? To make commercial financing a smooth and enjoyable experience for you.</p>
    </div>

    <section class="products">
      <div class="products-band"></div>
      <div class="products-rule"></div>
      <div class="products-label">Our Products</div>
      <div class="product p1">
        <div class="product-title">BRIDGE LOANS</div>
        <div class="product-photo" role="img" aria-label="Photo of a hand drafting architectural plans on a desk"></div>
      </div>
      <div class="product p2">
        <div class="product-title">DEVELOPMENT FINANCE</div>
        <div class="product-photo" role="img" aria-label="Photo of a multi-storey building under construction against blue sky"></div>
      </div>
      <div class="product p3">
        <div class="product-title">BUY-TO-LET MORTGAGES</div>
        <div class="product-photo" role="img" aria-label="Photo of a small model house with keys on a wooden table"></div>
      </div>
    </section>

    <footer class="footer">
      <div class="contact-line address">
        <svg width="14" height="20" viewBox="0 0 14 20"><path d="M7 0C3.1 0 0 3.1 0 7c0 5 7 13 7 13s7-8 7-13c0-3.9-3.1-7-7-7zm0 9.5A2.5 2.5 0 1 1 7 4.5a2.5 2.5 0 0 1 0 5z" fill="#fff"/></svg>
        <span>2140 Larkspur Road Anchorage, Alaska 34512</span>
      </div>
      <div class="contact-line reach">
        <span class="item">
          <svg width="12" height="20" viewBox="0 0 12 20"><rect x="1" y="1" width="10" height="18" rx="2" fill="none" stroke="#fff" stroke-width="2"/><rect x="4" y="15" width="4" height="2" fill="#fff"/></svg>
          555-201-4780
        </span>
        <span class="item">
          <svg width="16" height="12" viewBox="0 0 16 12"><rect x="0" y="0" width="16" height="12" fill="#fff"/><path d="M0 0 L8 7 L16 0" fill="none" stroke="#1f3d9c" stroke-width="1.6"/></svg>
          info@velmorafinance.com
        </span>
        <span class="item">
          <svg width="16" height="16" viewBox="0 0 16 16"><circle cx="8" cy="8" r="7" fill="none" stroke="#fff" stroke-width="1.5"/><ellipse cx="8" cy="8" rx="3" ry="7" fill="none" stroke="#fff" stroke-width="1.3"/><path d="M1 8H15" stroke="#fff" stroke-width="1.3"/></svg>
          www.velmorafinance.com
        </span>
      </div>
      <svg class="call-badge" width="56" height="56" viewBox="0 0 56 56">
        <circle cx="28" cy="28" r="27" fill="#23863f"/>
        <path d="M19 16c2-1 3 0 4 2l2 4c.5 1.5 0 2.5-1 3.2-.8.6-.8 1.5-.2 2.6 1.4 2.3 3.1 4 5.4 5.4 1.1.6 2 .6 2.6-.2.7-1 1.7-1.5 3.2-1l4 2c2 1 3 2 2 4-1.5 3-4.5 4.2-8 3-7-2.4-13-8.4-15.4-15.4-1.2-3.5 0-6.5 1.4-7.6z" fill="#fff"/>
      </svg>
      <div class="call-note">For mor info</div>
      <div class="call-number">555-318-6042</div>
    </footer>
  </article>
</div>
</body>
</html>
```